Flyer für Fußball-Förderverein
Zielgruppe
Wir sind der Fußball-Förderverein des SpVg Halmbeck.
Aufgabenstellung
1. Ziel des Flyers:
Der Flyer soll den Förderverein des SpVg Halmbeck bekannter machen und neue Mitglieder und Sponsoren gewinnen. Er soll darüber informieren, wie der Förderverein den Verein unterstützt und warum eine Mitgliedschaft oder eine Spende wichtig ist.
2. Zielgruppe:
Eltern der Kinder und Jugendlichen, die im SpVg Halmbeck Fußball spielen.
Lokale Unternehmen und potenzielle Sponsoren.
Vereinsmitglieder und Fußballinteressierte in der Region.
3. Hauptbotschaft:
„Unterstütze den SpVg Halmbeck – Gemeinsam für die Zukunft unseres Vereins und der Jugend!“
4. Inhalte:
Über den Förderverein:
Eine kurze Beschreibung des Fördervereins, warum er existiert und was er für den Verein und die Jugend tut.
Mitgliedschaft:
Informationen, wie man Mitglied im Förderverein werden kann. Vorteile und der Beitrag, der benötigt wird.
Spenden:
Möglichkeit der direkten Spende mit einem Hinweis auf steuerliche Vorteile (falls zutreffend). Möglicherweise auch die Angabe eines Spendenkontos.
Beispiele für die Verwendung von Mitteln:
Welche Projekte oder Anschaffungen wurden durch den Förderverein unterstützt (z.B. Trainingsmaterialien, Ausrüstung, Turniere, Jugendfahrten)?
Kontaktinformationen:
Ansprechpartner des Fördervereins mit Telefonnummer, E-Mail-Adresse und eventuell ein Link zur Webseite oder Social-Media-Profilen.
5. Designvorgaben:
Farben und Stil:
Die Vereinsfarben des SpVg Halmbeck sollten im Flyer dominieren (grün-weiß, etc.). Ein modernes, aber sportliches Design, das dynamisch wirkt und die Zielgruppe anspricht.
Logo:
Das Logo des SpVg Halmbeck sollte prominent platziert werden, ebenso das Logo des Fördervereins (falls vorhanden).
Bilder:
Verwendung von Bildern aus dem Vereinsleben, insbesondere von Kindern und Jugendlichen im Spielbetrieb oder bei Vereinsaktivitäten. Falls keine spezifischen Bilder vorhanden sind, können allgemeine Fußballbilde..

```html
<!DOCTYPE html>
<html lang="de">
<head>
<meta charset="utf-8">
<title>Flyer Förderverein SpVg Halmbeck</title>
<link rel="stylesheet" href="https://fonts.googleapis.com/css2?family=Russo+One&family=PT+Sans+Narrow:wght@400;700&display=swap">
<style>
:root{
  --bg:#a5a4a9;
  --paper:#f1f1ef;
  --green:#1f9a3c;
  --green-dark:#0d3b18;
  --green-deep:#062610;
  --ink:#2b2b2b;
  --muted:#666;
  --line:#b9b9b9;
  --white:#ffffff;
}
*{margin:0;padding:0;box-sizing:border-box}
html,body{width:1200px;height:3074px;overflow:hidden;background:var(--bg)}
body{font-family:"PT Sans Narrow",sans-serif;color:var(--ink);position:relative}
.spread{position:absolute;left:60px;width:1080px;height:764px;display:flex;box-shadow:0 18px 40px rgba(0,0,0,.25)}
.spread--outside{top:420px}
.spread--inside{top:1760px}
.panel{position:relative;width:360px;height:764px;overflow:hidden;background:var(--paper)}
.panel + .panel{border-left:1px solid rgba(0,0,0,.06)}
.headline{font-family:"Russo One",sans-serif;font-weight:400;text-transform:uppercase;line-height:1;letter-spacing:-.5px}
.headline--green{color:var(--green)}
.headline--white{color:var(--white)}
.copy{font-size:13px;line-height:1.45}
.copy p + p{margin-top:8px}
.photo{position:absolute}

/* outside left */
.support .photo{inset:0;background:linear-gradient(105deg,#2f5a26 0%,#4b7a33 45%,#d9dcd6 58%,#f0f0ee 64%,#5d8a3c 72%,#2c5222 100%)}
.support .headline{position:absolute;left:38px;top:54px;font-size:36px;width:300px}
.support .copy{position:absolute;left:38px;top:168px;width:210px;color:var(--white);font-size:13px}
.support .band{position:absolute;left:0;bottom:0;width:360px;height:150px}
.support .band-text{position:absolute;left:38px;bottom:20px;width:300px;color:var(--white);font-size:11px;line-height:1.45}

/* contact */
.contact{padding:56px 38px 0}
.contact .headline{font-size:31px;margin-bottom:16px}
.contact .block{margin-bottom:40px}
.contact .copy{font-size:12.5px;line-height:1.5}
.contact .person{margin-bottom:22px}
.contact strong{font-weight:700}

/* cover */
.cover .photo{left:0;top:0;width:360px;height:460px;background:radial-gradient(circle at 70% 40%,#5fb86e 0%,#1d7a35 30%,#0c3b18 65%,#061d0c 100%)}
.cover .edge{position:absolute;left:0;top:380px;width:360px;height:100px}
.brand{position:absolute;left:50%;top:70px;transform:translateX(-50%);width:200px;text-align:center;color:var(--white)}
.brand-dot{width:70px;height:70px;border-radius:50%;background:var(--white);margin:0 auto 14px}
.brand-name{font-family:"PT Sans Narrow",sans-serif;font-weight:700;font-size:16px;line-height:1.2;text-transform:uppercase}
.cover .title{position:absolute;left:38px;top:580px}
.cover .title-small{font-size:22px;color:var(--ink);margin-bottom:6px}
.cover .title-large{font-size:36px}
.cover .copy{position:absolute;left:38px;top:676px;width:250px;font-size:14px;color:#444}

/* inside left */
.about .headline{position:absolute;left:38px;top:54px;font-size:31px}
.about .copy{position:absolute;left:38px;top:110px;width:270px}
.about .photo{left:0;bottom:0;width:360px;height:250px;background:linear-gradient(180deg,#4d4541 0%,#5d5550 45%,#2f7d2a 70%,#1e5b1c 100%)}
.about .cut{position:absolute;left:0;top:500px;width:360px;height:40px}

/* inside middle */
.join{background:var(--green)}
.join .photo{left:20px;top:30px;width:320px;height:300px;border-radius:50%;background:radial-gradient(circle,#ffffff 0%,#f3faf4 35%,rgba(255,255,255,.35) 60%,rgba(255,255,255,0) 72%)}
.join .headline{position:absolute;left:38px;top:440px;font-size:24px;width:290px;line-height:1.1}
.join .copy{position:absolute;left:38px;top:520px;width:280px;color:var(--white)}
.join .copy strong{font-weight:700}

/* form */
.form{padding:56px 38px 0}
.form .headline{font-size:28px;margin-bottom:18px}
.check{display:flex;gap:10px;font-size:12px;line-height:1.4;margin-bottom:12px}
.box{flex:0 0 14px;height:14px;border:1.5px solid var(--green);margin-top:2px}
.field{display:flex;align-items:flex-end;gap:8px;font-size:10px;color:var(--muted);height:22px;border-bottom:1px solid var(--line)}
.field span{width:62px}
.fields{margin:6px 0 18px}
.legal{font-size:8.5px;line-height:1.4;color:var(--muted);margin:8px 0 10px}
.legal strong{color:var(--ink)}
</style>
</head>
<body>

<section class="spread spread--outside" aria-label="Flyer Außenseite">
  <article class="panel support">
    <div class="photo" role="img" aria-label="Foto: Rasenplatz mit weißer Seitenlinie und gezeichneter Spielerfigur"></div>
    <h2 class="headline headline--white">Sei dabei und unterstütze uns</h2>
    <div class="copy"><p>Bereits ab 1 € / pro Monat kannst du mit einer Mitgliedschaft als Privatperson oder als Firma den Förderverein und damit den Fussball Förderverein Halmbeck e.V. unterstützen.</p></div>
    <svg class="band" viewBox="0 0 360 150" preserveAspectRatio="none" aria-hidden="true">
      <polygon points="0,40 30,28 60,36 95,22 130,34 170,24 210,38 250,26 290,36 330,24 360,32 360,150 0,150" fill="#1f9a3c"/>
    </svg>
    <p class="band-text">Darüber hinaus sind natürlich auch höhere Beiträge oder einmalige Spenden möglich, die von der Einkommensteuer abgesetzt werden können. Desweiteren nehmen wir auch sehr gerne Sachspenden für Tombolas etc. entgegen.</p>
  </article>

  <article class="panel contact">
    <div class="block">
      <h2 class="headline headline--green">Kontakt</h2>
      <div class="copy"><strong>Fussball Förderverein Halmbeck e.V.</strong><br>Lindenweg 14<br>27399 Halmstedt - Halmbeck<br>foerderverein@spvg-halmbeck.de</div>
    </div>
    <div class="block">
      <h2 class="headline headline--green">Ansprechpartner</h2>
      <div class="copy person"><strong>Jonas Brettmann</strong><br>1. Vorsitzender<br>Tel. 04271/5820</div>
      <div class="copy person"><strong>Lars Wiebking</strong><br>2. Vorsitzender<br>Tel. 04271/5820</div>
      <div class="copy person"><strong>Timo Harms</strong><br>Kassenwart und Sportwart<br>Tel. 04271/5820</div>
    </div>
    <div class="block">
      <h2 class="headline headline--green">Bankverbindung</h2>
      <div class="copy"><strong>Bakname</strong><br>Kontonummer<br>BLZ<br>IBAN<br>Kontoinhaber</div>
    </div>
  </article>

  <article class="panel cover">
    <div class="photo" role="img" aria-label="Grün eingefärbtes Motiv eines Fußballs mit Farbspritzern"></div>
    <svg class="edge" viewBox="0 0 360 100" preserveAspectRatio="none" aria-hidden="true">
      <polygon points="0,40 40,58 80,44 120,66 160,50 200,72 240,56 280,74 320,60 360,70 360,100 0,100" fill="#f1f1ef"/>
    </svg>
    <div class="brand">
      <div class="brand-dot"></div>
      <div class="brand-name">Fussball Förderverein Halmbeck e.V.</div>
    </div>
    <div class="title">
      <div class="headline title-small">Unterstütze den</div>
      <div class="headline headline--green title-large">SpVg Halmbeck</div>
    </div>
    <p class="copy">Gemeinsam für die Zukunft unseres Vereins und der Jugend!</p>
  </article>
</section>

<section class="spread spread--inside" aria-label="Flyer Innenseite">
  <article class="panel about">
    <h2 class="headline headline--green">Wer sind wir</h2>
    <div class="copy">
      <p>Unser Fussball Verein SpVg Halmbeck umfasst rund XX Fussballer und Fussballerinnen im Alter von 4-65 Jahren.</p>
      <p>Im Vordergrund steht die individuelle Förderung der Spieler und erst dann der Tabellenplatz.</p>
      <p>Damit der Fussball weiterhin eine wichtige Rolle in unserer Stadt einnimmt, benötigen wir eure Hilfe und sind regelmäßig auf Spenden angewiesen. Schon der kleinste Betrag kann uns helfen, damit Trainingsmaterialien, Ausrüstung, Turniere oder Jugendfahrten finanziert werden können.</p>
    </div>
    <div class="photo" role="img" aria-label="Foto: Kinder beim Fußballspielen auf dem Rasen"></div>
    <svg class="cut" viewBox="0 0 360 40" preserveAspectRatio="none" aria-hidden="true">
      <polygon points="0,0 360,0 360,4 300,14 240,8 180,22 120,16 60,30 0,24" fill="#f1f1ef"/>
    </svg>
  </article>

  <article class="panel join">
    <div class="photo" role="img" aria-label="Weiße Illustration eines Fußballs mit Farbspritzern"></div>
    <h2 class="headline headline--white">Du möchtest Teil der Fussballfamilie werden?</h2>
    <div class="copy">
      <p>Dann komm zu uns und werde Mitglied in unserem Verein! Egal, ob als kleiner oder großer Anwärter oder als erfahrener Spieler – bei uns findest du ein Team, das zu dir passt.</p>
      <p><strong>Komm einfach zu einem unserer Trainingstermine vorbei und lerne uns persönlich kennen. Wir freuen uns auf dich!</strong></p>
    </div>
  </article>

  <article class="panel form">
    <h2 class="headline headline--green">Aufnahmeantrag</h2>
    <div class="check"><span class="box"></span><span>Ja, ich möchte Mitglied im Fussball Förderverein Halmbeck e.V. werden und damit den Fussball im Jugendbereich unterstützen.</span></div>
    <div class="fields">
      <div class="field"><span>Name / Firma</span></div>
      <div class="field"><span>Geb.-Datum</span></div>
      <div class="field"><span>Straße / Nr.</span></div>
      <div class="field"><span>PLZ / Ort</span></div>
      <div class="field"><span>E-Mail</span></div>
      <div class="field"><span>Telefon</span></div>
    </div>
    <div class="check"><span class="box"></span><span>Monatsbetrag 1,00 € (12,00 € im Jahr)</span></div>
    <div class="check"><span class="box"></span><span>Monatsbetrag ________ €</span></div>
    <p class="legal"><strong>SEPA-Lastschriftmandat:</strong> Ich ermächtige den Fussball Förderverein Halmbeck e.V., Zahlungen von meinem Konto mittels Lastschrift einzuziehen. Zugleich weise ich mein Kreditinstitut an, die vom Verein auf mein Konto gezogenen Lastschriften einzulösen. Ich kann innerhalb von acht Wochen, beginnend mit dem Belastungsdatum, die Erstattung des belasteten Betrages verlangen.</p>
    <div class="fields">
      <div class="field"><span>Name / Firma</span></div>
      <div class="field"><span>Bank</span></div>
      <div class="field"><span>IBAN</span></div>
      <div class="field"><span>Ort / Datum</span></div>
      <div class="field"><span>Unterschrift</span></div>
    </div>
  </article>
</section>

</body>
</html>
```